10' WIDE TRADE SHOW BACKDROP DESIGN

I need a 10' wide by 7'4" tall trade show back drop designed for my company. We are a carpet cleaning company. It is a display from birch displays and you can see the dimensions here.
http://www.birchdisplays.example/easy-fabric-pop-up-display-replacement-graphics.html

I will supply logo, ps art of some dogs we use as well as a picture of our van so you can match it a little. From there I need something very cool.

I will supply them via filehopper.example because the files are large.

Our website is www.brightweavecare.example if you would like to see a little about our company.

The final design should use our blue colors, emphasize Safer, Cleaner, Faster, Smarter. It should bring home the fact that we are a quality cleaner not a cheap cleaner.

Target Market(s)

Mid to high end home and business owners who will make decisions on floor cleaning

Industry/Entity Type

Trade

Colors
0455a3
3276b5
0592cd
34a7d8
86cae6
86acd3
ffffff

Requirements
Must have
• Logo + "Safer, Cleaner, Faster, Smarter"
Dalmation pic
website
"FREE CLEANING" ask for details
Nice to have
• should incorporate the feel of the van so I have included a couple of pictures of it.

```html
<!DOCTYPE html>
<html lang="en">
<head>
<meta charset="utf-8">
<title>Brightweave Floor Care – Trade Show Backdrop</title>
<link rel="stylesheet" href="https://fonts.googleapis.com/css2?family=Cabin+Sketch:wght@400;700&family=Schoolbell&family=Open+Sans:wght@400;700;800&display=swap">
<style>
  :root {
    --sky-blue: #0796d0;
    --deep-blue: #0455a3;
    --mid-blue: #2a8dd7;
    --ink-blue: #2e6db4;
    --link-blue: #1f5fae;
    --white: #ffffff;
    --pup-light: #f4f4f4;
    --pup-shade: #d9d9d9;
    --brand-grey: #6b6b6b;
  }
  * { margin: 0; padding: 0; box-sizing: border-box; }
  html, body { width: 1200px; height: 888px; overflow: hidden; background: var(--white); }
  .backdrop { position: relative; width: 1200px; height: 888px; overflow: hidden; background: var(--white); }
  .backdrop-shapes { position: absolute; inset: 0; }

  .slogan {
    position: absolute; left: 745px; top: 148px; width: 430px;
    text-align: center; list-style: none;
    font-family: "Cabin Sketch", cursive; font-weight: 700;
    font-size: 54px; line-height: 60px; letter-spacing: 3px;
    color: var(--ink-blue); text-transform: uppercase;
  }
  .website {
    position: absolute; left: 745px; top: 474px; width: 430px; text-align: center;
    font-family: "Open Sans", sans-serif; font-size: 28px; color: var(--link-blue);
  }
  .offer {
    position: absolute; left: 0; top: 340px; width: 256px; text-align: center; color: var(--white);
  }
  .offer-title {
    font-family: "Schoolbell", cursive; font-weight: 400;
    font-size: 46px; line-height: 60px;
    text-shadow: 2px 3px 4px rgba(0, 40, 90, 0.55);
  }
  .offer-note {
    margin-top: 34px; font-family: "Open Sans", sans-serif; font-size: 22px;
  }
  .brand {
    position: absolute; left: 44px; top: 748px; width: 320px; text-align: center;
    font-family: "Open Sans", sans-serif; font-weight: 800; color: var(--brand-grey);
    line-height: 1.1;
  }
  .brand-name { font-size: 38px; letter-spacing: 1px; }
  .brand-sub { font-size: 20px; letter-spacing: 3px; }
  .pups-photo {
    position: absolute; left: 360px; top: 646px; width: 840px; height: 242px;
    background: linear-gradient(180deg, var(--white) 0%, var(--pup-light) 55%, var(--pup-shade) 100%);
  }
</style>
</head>
<body>
<main class="backdrop">
  <svg class="backdrop-shapes" width="1200" height="888" viewBox="0 0 1200 888" aria-hidden="true">
    <rect class="sky-band" x="0" y="0" width="1200" height="493" fill="var(--sky-blue)"/>
    <circle class="slogan-ring" cx="893" cy="296" r="340" fill="var(--deep-blue)"/>
    <circle class="slogan-disc" cx="945" cy="306" r="290" fill="var(--white)"/>
    <circle class="offer-ring" cx="143" cy="452" r="190" fill="var(--deep-blue)"/>
    <circle class="offer-disc" cx="136" cy="447" r="150" fill="var(--mid-blue)"/>
  </svg>

  <ul class="slogan">
    <li>Safer</li>
    <li>Cleaner</li>
    <li>Faster</li>
    <li>Smarter</li>
  </ul>
  <p class="website">www.brightweavecare.example</p>

  <div class="offer">
    <h2 class="offer-title">Free<br>Cleaning</h2>
    <p class="offer-note">*ask for details</p>
  </div>

  <div class="brand">
    <div class="brand-name">BRIGHTWEAVE</div>
    <div class="brand-sub">FLOOR CARE</div>
  </div>

  <div class="pups-photo" role="img" aria-label="Photo of a row of eight Dalmatian puppies sitting on a white floor"></div>
</main>
</body>
</html>
```